Business cards and logo for kitchen and bath remodeling company

We want an elegant card but that calls attention something unique and when people see it they remember us. A log that we can use for our own. We are a kitchen and bathroom remodeling company. We are 3 partners staring the company we are located in seattle washington usa. We try to give the best experience and luxury look in our projects and we are looking to show that in our cards. I added a sample of a card I really like. I like the black and gold look but gray blue or green in a metallic look would look nice. I'm open to any color.

Target Market(s)

Home owners.

Industry/Entity Type

Construction

Contact Information for Business Card

Larchmont and Vey builders

Colors

Designer to choose colors to be used in the design.

Requirements
Must have
• Make a Logo
• Logo to be unique
• Name of company larchmont and vey builders
Nice to have
• Have a good color scheme
• Front design to connect with back of card

```html
<!DOCTYPE html>
<html lang="en">
<head>
<meta charset="utf-8">
<title>Larchmont and Vey Builders – Business Card</title>
<link rel="stylesheet" href="https://fonts.googleapis.com/css2?family=Montserrat:wght@600;700&family=Arimo:wght@400;700&display=swap">
<style>
  :root {
    --stage: #1c1c1e;
    --card: #121114;
    --gold: #b99c74;
    --silver: #c9c9cc;
    --ink-light: #f2f2f2;
    --divider: #3a3a3e;
  }
  * { box-sizing: border-box; margin: 0; padding: 0; }
  html, body {
    width: 1200px;
    height: 900px;
    overflow: hidden;
    background: var(--stage);
  }
  .stage {
    position: relative;
    width: 1200px;
    height: 900px;
  }
  .card {
    position: absolute;
    left: 290px;
    width: 620px;
    height: 354px;
    background: var(--card);
    box-shadow: 0 10px 30px rgba(0,0,0,.55);
  }
  .card--back { top: 70px; }
  .card--front { top: 476px; }

  /* Back side */
  .back-brand {
    position: absolute;
    top: 120px;
    left: 0;
    right: 0;
    display: flex;
    justify-content: center;
    align-items: center;
    gap: 14px;
    font-family: "Montserrat", sans-serif;
    font-weight: 700;
    font-size: 28px;
    letter-spacing: 2px;
    color: var(--silver);
    text-transform: uppercase;
  }
  .brand-square {
    width: 22px;
    height: 22px;
    border: 2px solid currentColor;
  }
  .back-web {
    position: absolute;
    bottom: 62px;
    left: 0;
    right: 0;
    text-align: center;
    font-family: "Arimo", sans-serif;
    font-size: 14px;
    letter-spacing: 1.5px;
    color: var(--silver);
  }

  /* Front side */
  .front-brand {
    position: absolute;
    left: 30px;
    top: 0;
    width: 300px;
    height: 100%;
    display: flex;
    flex-direction: column;
    justify-content: center;
    align-items: center;
    gap: 16px;
    font-family: "Montserrat", sans-serif;
    font-weight: 700;
    color: var(--gold);
    text-transform: uppercase;
    text-align: center;
  }
  .front-brand .brand-square { width: 30px; height: 30px; }
  .front-brand-name {
    font-size: 24px;
    line-height: 1.25;
    letter-spacing: 1px;
  }
  .divider {
    position: absolute;
    left: 352px;
    top: 40px;
    bottom: 40px;
    width: 1px;
    background: var(--divider);
  }
  .contact {
    position: absolute;
    left: 378px;
    top: 78px;
    font-family: "Arimo", sans-serif;
    color: var(--ink-light);
    font-size: 15px;
    line-height: 1.3;
  }
  .contact-name {
    font-weight: 700;
    font-size: 17px;
    letter-spacing: 1px;
    color: var(--gold);
    text-transform: uppercase;
  }
  .contact-role { margin-bottom: 12px; }
  .contact-line {
    display: flex;
    align-items: center;
    gap: 7px;
    margin-bottom: 3px;
  }
  .contact-line svg { width: 12px; height: 12px; fill: var(--ink-light); flex: none; }
  .contact-address { margin-top: 10px; }
</style>
</head>
<body>
<main class="stage">

  <section class="card card--back" aria-label="Card back">
    <div class="back-brand">
      <span class="brand-square"></span>
      <span>Larchmont &amp; Vey</span>
    </div>
    <p class="back-web">www.larchmontvey.com</p>
  </section>

  <section class="card card--front" aria-label="Card front">
    <div class="front-brand">
      <span class="brand-square"></span>
      <span class="front-brand-name">Larchmont and Vey<br>Builders</span>
    </div>

    <div class="divider"></div>

    <div class="contact">
      <p class="contact-name">Daniel Hartwell</p>
      <p class="contact-role">Managing Director</p>
      <p class="contact-line">
        <svg viewBox="0 0 24 24" aria-hidden="true"><path d="M6.6 10.8a15.1 15.1 0 0 0 6.6 6.6l2.2-2.2a1 1 0 0 1 1-.25 11.4 11.4 0 0 0 3.6.57 1 1 0 0 1 1 1V20a1 1 0 0 1-1 1A17 17 0 0 1 3 4a1 1 0 0 1 1-1h3.5a1 1 0 0 1 1 1c0 1.25.2 2.45.57 3.57a1 1 0 0 1-.25 1z"/></svg>
        044-987 654 321
      </p>
      <p class="contact-line">
        <svg viewBox="0 0 24 24" aria-hidden="true"><path d="M2 5h20v14H2z M2 5l10 8 10-8" fill="none" stroke="#f2f2f2" stroke-width="2"/></svg>
        info@larchmontvey.com
      </p>
      <p class="contact-line">
        <svg viewBox="0 0 24 24" aria-hidden="true"><circle cx="12" cy="12" r="10"/></svg>
        www.larchmontvey.com
      </p>
      <p class="contact-address">421, Address line here<br>Country Name, 45452</p>
    </div>
  </section>

</main>
</body>
</html>
```